Luxury Brand Real Estate For Sale sign

**Update** I've added some examples from the internet of other signs that have a look similar to what I would like to see. I do not want my personal name in the sign. And the word FOR SALE Does not need to be so large - it can be more subtle.
I want to create a Real Estate for sale sign for my company that will be used for luxury/higher end real estate listings. I’m sharing my business card as well as a logo with new teal color to show what we're moving towards: we’re using Teal, white, black and gold.
Hoping the sign is simple, sophisticated and eye catching.
The sign should be 24" wide by 30" tall including the company name: Harbor Crest Realty Group and our logo, office phone number 727-555-0148 and website www.hcrgexample.com the words "For Sale"
Optional to add this e-mail address info@hcrgexample.com to the sign
Target Market(s)
Luxury home buyers
Industry/Entity Type
Real Estate
Look and feel

```html
<!DOCTYPE html>
<html lang="en">
<head>
<meta charset="utf-8">
<title>Harbor Crest Realty Group – For Sale Sign</title>
<link href="https://fonts.googleapis.com/css2?family=Bebas+Neue&family=Josefin+Sans:wght@300&family=Poppins:wght@700&display=swap" rel="stylesheet">
<style>
  :root {
    --gold: #c2a020;
    --gold-light: #e8c055;
    --gold-deep: #d6ae3a;
    --black: #000000;
    --teal: #0e8380;
    --white: #ffffff;
  }
  html, body {
    margin: 0;
    padding: 0;
    overflow: hidden;
    background: var(--gold);
  }
  .sign {
    display: block;
    width: 962px;
    height: 1200px;
  }
  .brand-name {
    font-family: "Josefin Sans", "Montserrat", sans-serif;
    font-weight: 300;
    fill: var(--black);
  }
  .headline {
    font-family: "Bebas Neue", "Oswald", sans-serif;
  }
  .contact-web {
    font-family: "Poppins", "Montserrat", sans-serif;
    font-weight: 700;
    fill: var(--black);
  }
</style>
</head>
<body>
<svg class="sign" viewBox="0 0 962 1200" xmlns="http://www.w3.org/2000/svg" aria-label="Harbor Crest Realty Group for sale sign">
  <defs>
    <linearGradient id="headline-gold" x1="0" y1="0" x2="0" y2="1">
      <stop offset="0" stop-color="var(--gold-light)"/>
      <stop offset="1" stop-color="var(--gold-deep)"/>
    </linearGradient>
  </defs>

  <!-- background -->
  <rect class="sign-bg" x="0" y="0" width="962" height="1200" fill="var(--gold)"/>

  <!-- brand header -->
  <g class="brand-header">
    <rect class="brand-square" x="165" y="118" width="60" height="60" fill="var(--black)"/>
    <rect class="brand-divider" x="357" y="62" width="3" height="178" fill="var(--black)"/>
    <text class="brand-name" x="396" y="146" font-size="41" textLength="446" lengthAdjust="spacingAndGlyphs">HARBOR CREST</text>
    <text class="brand-name" x="395" y="181" font-size="25" textLength="296" lengthAdjust="spacing">REALTY GROUP</text>
  </g>

  <!-- black headline band -->
  <g class="headline-band">
    <rect x="3" y="265" width="959" height="483" fill="var(--black)"/>
    <text class="headline" x="125" y="529" font-size="279" fill="url(#headline-gold)" textLength="720" lengthAdjust="spacingAndGlyphs">FOR SALE</text>
    <text class="headline" x="126" y="684" font-size="169" fill="var(--white)" textLength="726" lengthAdjust="spacingAndGlyphs">727-555-0148</text>
  </g>

  <!-- teal website band -->
  <g class="web-band">
    <rect x="3" y="748" width="959" height="135" fill="var(--teal)"/>
    <text class="contact-web" x="124" y="834" font-size="66" textLength="736" lengthAdjust="spacingAndGlyphs">www.hcrgexample.com</text>
  </g>

  <!-- email -->
  <g class="email-block">
    <g class="mail-icon" transform="translate(441 921)">
      <rect x="0" y="0" width="96" height="79" fill="var(--black)"/>
      <polyline points="2,2 46,44 50,44 94,2" fill="none" stroke="var(--gold)" stroke-width="4" stroke-linejoin="round"/>
      <line x1="2" y1="78" x2="31" y2="48" stroke="var(--gold)" stroke-width="4"/>
      <line x1="94" y1="78" x2="65" y2="48" stroke="var(--gold)" stroke-width="4"/>
    </g>
    <text class="contact-web" x="142" y="1069" font-size="66" textLength="697" lengthAdjust="spacingAndGlyphs">info@hcrgexample.com</text>
  </g>
</svg>
</body>
</html>
```